Tellvora business expansion job ad, join our team

Im needing a business expansion job Ad for tellvora. THis Ad will represent our car dealership hiring for multiple job positions which include. Automotive service positions, Sales consultants, collection agents, finance and underwriting and management. We are a Buy Here Pay Here dealership that is growing rapidly and moving into a new location, Business Expansion id a key term I would like to use. We are adding team members. We also need to be aware of Tellvoras image sizing so it will appear well.

Target Market(s)

employment, job ad

Colors
0054AA
0677BA
7BADD7
CADEEF
E8F1F8

Requirements
Must have
• Business Expansion , Join our team
Nice to have
• our logo

```html
<!DOCTYPE html>
<html lang="en">
<head>
<meta charset="utf-8">
<title>Tellvora – Business Expansion, We're Hiring</title>
<link rel="stylesheet" href="https://fonts.googleapis.com/css2?family=Righteous&family=Roboto+Condensed:wght@700&display=swap">
<style>
  :root {
    --page: #ffffff;
    --panel: #02548F;
    --frame: #1B8FC8;
    --tab: #1D8AC4;
    --card-top: #F4F5F6;
    --card-bottom: #DADCDF;
    --headline: #0A4F8E;
    --exclaim: #1C5E8C;
    --ink-light: #ffffff;
    --ink-soft: #CADEEF;
    --rule: #CADEEF;
    --art-light: #E8F1F8;
    --art-mid: #7BADD7;
  }
  html, body {
    margin: 0;
    padding: 0;
    width: 1200px;
    height: 1112px;
    overflow: hidden;
    background: var(--page);
  }
  .hiring-ad {
    display: block;
    width: 1200px;
    height: 1112px;
  }
  .headline {
    font-family: "Righteous", "Arial Rounded MT Bold", sans-serif;
    fill: var(--headline);
  }
  .tab-label,
  .expansion-line,
  .role-item,
  .contact-line {
    font-family: "Roboto Condensed", "Arial Narrow", sans-serif;
    font-weight: 700;
    fill: var(--ink-light);
  }
  .expansion-line { fill: var(--ink-soft); }
</style>
</head>
<body>
<svg class="hiring-ad" viewBox="0 0 1200 1112" xmlns="http://www.w3.org/2000/svg">
  <defs>
    <linearGradient id="cardFill" x1="0" y1="0" x2="0" y2="1">
      <stop offset="0" stop-color="var(--card-top)"/>
      <stop offset="1" stop-color="var(--card-bottom)"/>
    </linearGradient>
    <linearGradient id="mascotFill" x1="0" y1="0" x2="1" y2="1">
      <stop offset="0" stop-color="var(--art-light)"/>
      <stop offset="1" stop-color="var(--art-mid)"/>
    </linearGradient>
  </defs>

  <!-- main blue panel -->
  <rect class="panel" x="38" y="0" width="1107" height="1075" fill="var(--panel)"/>

  <!-- headline card -->
  <rect class="headline-card" x="361" y="165" width="749" height="403" rx="22"
        fill="url(#cardFill)" stroke="var(--frame)" stroke-width="9"/>

  <!-- mascot medallion -->
  <circle class="medallion" cx="318" cy="372" r="239" fill="url(#cardFill)"
          stroke="var(--frame)" stroke-width="13"/>
  <circle class="mascot" cx="318" cy="372" r="226" fill="url(#mascotFill)"
          role="img" aria-label="Friendly silver and blue robot mascot waving, wearing a visor helmet"/>

  <!-- headline -->
  <text class="headline" x="584" y="368" font-size="190" textLength="420" lengthAdjust="spacingAndGlyphs">WE´RE</text>
  <text class="headline" x="584" y="510" font-size="160" textLength="420" lengthAdjust="spacingAndGlyphs">HIRING</text>
  <g class="exclaim" fill="var(--exclaim)">
    <path d="M1022 249 H1071 L1064 456 H1030 Z"/>
    <circle cx="1048" cy="490" r="24"/>
  </g>

  <!-- join tab -->
  <path class="join-tab" d="M510 568 H1046 V632 Q1046 653 1025 653 H531 Q510 653 510 632 Z" fill="var(--tab)"/>
  <text class="tab-label" x="778" y="633" font-size="60" text-anchor="middle">JOIN OUR TEAM</text>

  <!-- expansion statement -->
  <text class="expansion-line" x="88" y="728" font-size="56">BUSINESS EXPANSION · NEW LOCATION</text>

  <!-- open positions -->
  <g class="role-list" font-size="42">
    <text class="role-item" x="88" y="796">- AUTOMOTIVE SERVICE</text>
    <text class="role-item" x="88" y="852">- SALES CONSULTANTS</text>
    <text class="role-item" x="88" y="908">- MANAGEMENT</text>
    <text class="role-item" x="600" y="796">- COLLECTION AGENTS</text>
    <text class="role-item" x="600" y="852">- FINANCE &amp; UNDERWRITING</text>
  </g>

  <line class="divider" x1="76" y1="961" x2="1110" y2="961" stroke="var(--rule)" stroke-width="2"/>

  <text class="contact-line" x="592" y="1049" font-size="56" text-anchor="middle">MAIL US AT : INFO@TELLVORA-JOBS.COM</text>
</svg>
</body>
</html>
```